Brochure design for HVAC Company

A classic tri-fold brochure design for an air conditioning, refrigeration, and heating company. Would like the designs to be simple (uncluttered), professional, and pull in the logo colors. Attached is the logo and a business card designs. The company name is Bluestem Valley Air Conditioning, Refrigeration, and Heating.

Target Market(s)

Businesses normally food establishments for refrigeration and ice machines. Looking to sell them on maintenance plan: Gold, Silver, and Bronze. The material should help them to understand the services offered: Maintenance, Servicing and Troubleshooting, and Installations of ice machines, commercial refrigeration, and walk-in freezers and air conditioning (duct, ductless, and rooftop)

Industry/Entity Type

Hvac

Font styles to use
Sans Serif

Requirements
Must have
• Include standard information, such as company name, at least two types of contact information (phone, email and post office address), a logo and tagline. It should also include a headline on the front and two or three brief items outlining benefits your organization can provide.
• Tagline is approximately 14 words and 66 characters.
• Looking to inform customers of services offered: maintenance three plans gold, silver, and bronze, servicing and troubleshooting, and installation.
• Products Serviced, maintained, and installed: Commercial refrigeration, Ice Machines, Air Conditioning (both duct, ductless, and rooftop), walk in freezers.
• Call to action is $100 off on signed maintenance contract. $50 off on first service call.
• Use lorem ipsum text to complement the details of the above information. I will add it later before printing.
• Use logo color scheme and any other colors that complement it.
• Would like this to be a word template.
Nice to have
• Can you make this a Microsoft Word template? Sketch is good, or adobe cs4 format.
Should not have
• Photos should NOT be focused on the homeowner. Should BE focused on the commercial side of the business. Photos can be from any of these product areas: commercial refrigeration, ice machine, walk in freezer boxes, and light roof top ac and heating units.

```html
<!DOCTYPE html>
<html lang="en">
<head>
<meta charset="utf-8">
<title>Bluestem Valley – Tri-fold Brochure</title>
<link rel="stylesheet" href="https://fonts.googleapis.com/css2?family=Oswald:wght@500;700&family=Roboto+Condensed:wght@400;700&display=swap">
<style>
:root{
  --blue:#2b4aa0;
  --blue-dark:#1f3a86;
  --orange:#ec5a1c;
  --orange-light:#f47a3a;
  --peach:#f8cdb2;
  --peach-light:#fde8da;
  --white:#ffffff;
  --ink:#2c3550;
  --bg:#e6e6e6;
  --photo-cool:linear-gradient(160deg,#e9ecef,#c3c9cf);
  --photo-steel:linear-gradient(160deg,#bfc6cc,#7d868e);
  --photo-warm:linear-gradient(160deg,#4a6fa8,#d9874c);
}
*{box-sizing:border-box;margin:0;padding:0}
html,body{width:1053px;height:1200px;overflow:hidden;background:var(--bg)}
body{position:relative;font-family:"Roboto Condensed",Arial,sans-serif;color:var(--white)}
.spread{position:absolute;left:24px;width:1005px;height:565px;display:flex;box-shadow:0 3px 10px rgba(0,0,0,.18)}
.spread--outside{top:24px}
.spread--inside{top:611px}
.panel{position:relative;width:335px;height:100%;overflow:hidden}
.panel--blue{background:var(--blue)}
.panel--orange{background:var(--orange)}
.panel--white{background:var(--white);color:var(--ink)}
.photo{display:block;border-radius:2px}
.photo--cool{background:var(--photo-cool)}
.photo--steel{background:var(--photo-steel)}
.photo--warm{background:var(--photo-warm)}

/* feature blocks */
.features{position:absolute;left:0;right:0;top:22px}
.feature{padding:0 20px;margin-top:16px}
.feature:first-child{margin-top:0}
.feature__head{display:flex;align-items:center;margin-bottom:7px}
.feature__icon{width:26px;height:26px;border-radius:50%;background:var(--orange);border:3px solid var(--white);flex:none;position:relative;z-index:1}
.feature__tag{background:var(--orange);font-family:"Oswald",sans-serif;font-weight:500;font-size:14px;letter-spacing:.3px;padding:3px 14px 3px 18px;margin-left:-10px;border-radius:0 14px 14px 0}
.feature__text{font-size:10.8px;line-height:1.3;text-align:justify}

/* coupons */
.coupon{position:absolute;left:18px;right:18px;display:flex;height:96px}
.coupon__photo{width:84px;height:100%;flex:none}
.coupon__rows{flex:1;display:flex;flex-direction:column;gap:4px;margin-left:4px}
.coupon__row{flex:1;display:flex}
.coupon__value{background:var(--white);width:96px;display:flex;align-items:center;justify-content:center;gap:2px}
.coupon__cur{color:var(--orange);font-family:"Oswald",sans-serif;font-weight:700;font-size:15px;align-self:flex-end;margin-bottom:6px}
.coupon__num{color:var(--blue);font-family:"Oswald",sans-serif;font-weight:700;font-size:34px;line-height:1}
.coupon__off{color:var(--orange);font-family:"Oswald",sans-serif;font-size:9px;writing-mode:vertical-rl;transform:rotate(180deg);font-weight:700}
.coupon__terms{flex:1;display:flex;flex-direction:column;justify-content:center;padding:0 8px;font-family:"Oswald",sans-serif;line-height:1}
.coupon__terms b{font-size:17px;font-weight:700}
.coupon__terms small{font-size:9px;font-weight:500;margin-top:2px;color:var(--white)}
.coupon--on-blue .coupon__terms{background:var(--orange)}
.coupon--on-orange .coupon__terms{background:var(--blue)}
.coupon--on-orange .coupon__terms b{color:var(--orange-light)}

/* contact panel */
.contact{position:absolute;inset:14px;border:1.5px solid rgba(255,255,255,.75);border-radius:6px;display:flex;flex-direction:column;align-items:center;justify-content:center;text-align:center}
.contact__mark{width:54px;height:54px;border-radius:50%;border:2px solid var(--white);margin-bottom:14px}
.contact__title{font-family:"Oswald",sans-serif;font-weight:500;font-size:17px;letter-spacing:.5px;margin-bottom:12px}
.contact__lines{font-size:10.5px;line-height:1.4}
.contact__rule{width:30px;height:1px;background:var(--white);margin:10px auto}

/* cover */
.brand{display:flex;align-items:center;gap:10px;padding:22px 22px 0}
.brand__dot{width:40px;height:40px;border-radius:50%;background:var(--orange);flex:none}
.brand__name{font-weight:700;font-size:27px;line-height:.95;color:var(--blue)}
.brand__tagline{font-size:8.2px;letter-spacing:.8px;color:var(--blue);font-weight:700;padding:6px 22px 0 72px}
.cover-photo{position:absolute;left:22px;right:22px;top:104px;height:330px}
.cover-band{position:absolute;left:22px;right:22px;top:434px;height:78px;background:var(--blue);padding:10px 16px;text-align:center}
.cover-band h1{font-family:"Oswald",sans-serif;font-weight:700;font-size:30px;color:var(--orange-light);line-height:1;letter-spacing:.5px}
.cover-band p{font-size:10.5px;line-height:1.25;margin-top:5px;color:var(--white)}

/* inside left: products */
.products-hero{position:absolute;left:0;right:0;top:0;height:150px}
.product{position:absolute;left:18px;right:16px;display:flex;gap:10px}
.product__thumb{width:86px;height:64px;flex:none}
.product__name{font-family:"Oswald",sans-serif;font-weight:500;font-size:12px;text-decoration:underline;margin-bottom:2px;letter-spacing:.2px}
.product__text{font-size:10.8px;line-height:1.22}

/* services table */
.services{position:absolute;left:14px;right:14px;top:14px}
.services__head{display:grid;grid-template-columns:1fr 58px 58px 58px;background:var(--blue);color:var(--white);height:40px;align-items:center;border-bottom:4px solid var(--orange)}
.services__title{font-family:"Oswald",sans-serif;font-weight:500;font-size:12.5px;padding-left:10px}
.services__plan{text-align:center;font-size:9px;line-height:1.15;border-left:1px solid rgba(255,255,255,.5);font-weight:700}
.services__plan small{display:block;font-weight:400;font-size:7.5px}
.srow{display:grid;grid-template-columns:1fr 58px 58px 58px;height:15.6px;align-items:center;font-size:10px;color:var(--ink)}
.srow:nth-child(odd){background:var(--peach-light)}
.srow:nth-child(even){background:var(--white)}
.srow span{padding-left:12px}
.srow i{justify-self:center;width:4px;height:4px;border-radius:50%;background:#8a7a72}
.srow em{display:block}
.srow--cat{background:var(--orange)!important;color:var(--white);font-weight:700}
.services__note{position:absolute;left:22px;right:22px;bottom:12px;font-size:11px;color:var(--ink);text-align:center;line-height:1.25}

/* inside right */
.feature-photo{position:absolute;left:18px;right:18px}
.banner{position:absolute;left:30px;right:30px;background:var(--orange);font-family:"Oswald",sans-serif;font-weight:500;font-size:13.5px;text-align:center;padding:3px 0;letter-spacing:.3px}
.body-copy{position:absolute;left:24px;right:24px;font-size:10.5px;line-height:1.28;text-align:justify}
.points{position:absolute;left:24px;right:24px;bottom:16px;display:grid;grid-template-columns:1fr 1fr;gap:5px 14px;font-family:"Oswald",sans-serif;font-weight:500;font-size:13px;line-height:18px}
.points li{list-style:none;display:flex;align-items:center;gap:6px}
.points li::before{content:"";width:12px;height:12px;border-radius:50%;background:var(--orange);border:2px solid var(--white);flex:none}
</style>
</head>
<body>

<!-- OUTSIDE SPREAD -->
<section class="spread spread--outside">
  <div class="panel panel--blue">
    <div class="features">
      <div class="feature">
        <div class="feature__head"><span class="feature__icon"></span><span class="feature__tag">VETERES PHILOSOPHORUM</span></div>
        <p class="feature__text">Lorem ipsum dolor sit amet, consectetur adipiscing elit. Quid autem habent admirationis, cum prope accesseris? An hoc usque quaque, aliter in vita? Non igitur de improbo, sed de callido improbo quaerimus, qualis Q. Nam quibus rebus efficiuntur voluptates, eae non sunt in potestate sapientis.</p>
      </div>
      <div class="feature">
        <div class="feature__head"><span class="feature__icon"></span><span class="feature__tag">VERBORUM MAGNIFICENTIA</span></div>
        <p class="feature__text">Lorem ipsum dolor sit amet, consectetur adipiscing elit. Quid autem habent admirationis, cum prope accesseris? An hoc usque quaque, aliter in vita? Non igitur de improbo, sed de callido improbo quaerimus, qualis Q. Nam quibus rebus efficiuntur voluptates, eae non sunt in potestate sapientis.</p>
      </div>
      <div class="feature">
        <div class="feature__head"><span class="feature__icon"></span><span class="feature__tag">CONGRESSUS COPULATIONES</span></div>
        <p class="feature__text">Lorem ipsum dolor sit amet, consectetur adipiscing elit. Quid autem habent admirationis, cum prope accesseris? An hoc usque quaque, aliter in vita? Non igitur de improbo, sed de callido improbo quaerimus, qualis Q. Negare non possum.</p>
      </div>
    </div>
    <div class="coupon coupon--on-blue" style="bottom:18px">
      <div class="coupon__photo photo photo--warm" role="img" aria-label="Smiling service technician in work uniform holding a tablet"></div>
      <div class="coupon__rows">
        <div class="coupon__row">
          <div class="coupon__value"><span class="coupon__cur">$</span><span class="coupon__num">100</span><span class="coupon__off">OFF</span></div>
          <div class="coupon__terms"><b>ON SIGNED</b><small>MAINTENANCE CONTRACT.</small></div>
        </div>
        <div class="coupon__row">
          <div class="coupon__value"><span class="coupon__cur">$</span><span class="coupon__num">50</span><span class="coupon__off">OFF</span></div>
          <div class="coupon__terms"><b>ON FIRST</b><small>SERVICE CALL.</small></div>
        </div>
      </div>
    </div>
  </div>

  <div class="panel panel--orange">
    <div class="contact">
      <div class="contact__mark"></div>
      <h2 class="contact__title">CONTACT US</h2>
      <p class="contact__lines">PO Box 918<br>Meadowbrook, NY 11802<br>Lic. H5108823400</p>
      <div class="contact__rule"></div>
      <p class="contact__lines">516.555.0142<br>dana@bluestemhvac.com<br>www.bluestemhvac.com</p>
    </div>
  </div>

  <div class="panel panel--white">
    <div class="brand">
      <span class="brand__dot"></span>
      <span class="brand__name">BLUESTEM<br>VALLEY</span>
    </div>
    <p class="brand__tagline">AIR CONDITIONING • REFRIGERATION • HEATING</p>
    <div class="cover-photo photo photo--cool" role="img" aria-label="Commercial walk-in cold room with ceiling evaporator fans and stacked crates"></div>
    <div class="cover-band">
      <h1>LOREM IPSUM</h1>
      <p>Negare non possum. Huic mori optimum esse propter desperationem sapientiae, illi propter spem vivere.</p>
    </div>
  </div>
</section>

<!-- INSIDE SPREAD -->
<section class="spread spread--inside">
  <div class="panel panel--orange">
    <div class="products-hero photo photo--steel" role="img" aria-label="Silver insulated ductwork running along a commercial ceiling"></div>
    <div class="product" style="top:160px">
      <div class="product__thumb photo photo--warm" role="img" aria-label="Lit commercial refrigerated display cases"></div>
      <div><h3 class="product__name">COMMERCIAL REFRIGERATION</h3><p class="product__text">Equidem etiam Epicurum, in physicis quidem, Democriteum puto. Respondeat totidem verbis. Nemo igitur esse beatus potest.</p></div>
    </div>
    <div class="product" style="top:236px">
      <div class="product__thumb photo photo--cool" role="img" aria-label="Ice machine bin filled with ice"></div>
      <div><h3 class="product__name">ICE MACHINES</h3><p class="product__text">Equidem etiam Epicurum, in physicis quidem, Democriteum puto. Respondeat totidem verbis. Nemo igitur esse beatus potest.</p></div>
    </div>
    <div class="product" style="top:312px">
      <div class="product__thumb photo photo--steel" role="img" aria-label="Row of rooftop air conditioning condenser units"></div>
      <div><h3 class="product__name">AIR CONDITIONING</h3><p class="product__text">(both duct, ductless, and rooftop) physicis quidem, Democriteum puto. Respondeat totidem verbis.</p></div>
    </div>
    <div class="product" style="top:388px">
      <div class="product__thumb photo photo--cool" role="img" aria-label="Walk-in freezer interior with evaporator fans"></div>
      <div><h3 class="product__name">WALK IN FREEZERS</h3><p class="product__text">Equidem etiam Epicurum, in physicis quidem, Democriteum puto. Respondeat totidem verbis.</p></div>
    </div>
    <div class="coupon coupon--on-orange" style="bottom:14px;height:84px">
      <div class="coupon__photo photo photo--warm" role="img" aria-label="Smiling service technician in work uniform holding a tablet"></div>
      <div class="coupon__rows">
        <div class="coupon__row">
          <div class="coupon__value"><span class="coupon__cur">$</span><span class="coupon__num">100</span><span class="coupon__off">OFF</span></div>
          <div class="coupon__terms"><b>ON SIGNED</b><small>MAINTENANCE CONTRACT.</small></div>
        </div>
        <div class="coupon__row">
          <div class="coupon__value"><span class="coupon__cur">$</span><span class="coupon__num">50</span><span class="coupon__off">OFF</span></div>
          <div class="coupon__terms"><b>ON FIRST</b><small>SERVICE CALL.</small></div>
        </div>
      </div>
    </div>
  </div>

  <div class="panel panel--white">
    <div class="services">
      <div class="services__head">
        <span class="services__title">SERVICES OFFERED:</span>
        <span class="services__plan">GOLD<small>Rs 15,000</small></span>
        <span class="services__plan">SILVER<small>Rs 10,000</small></span>
        <span class="services__plan">BRONZE<small>Rs 5,000</small></span>
      </div>
      <div class="services__body">
        <div class="srow srow--cat"><span>fortunae facile veteres</span><em></em><em></em><em></em></div>
        <div class="srow"><span>Varietates</span><i></i><i></i><i></i></div>
        <div class="srow"><span>autem</span><i></i><i></i><em></em></div>
        <div class="srow"><span>iniurasque</span><i></i><em></em><i></i></div>
        <div class="srow"><span>fortunae</span><i></i><em></em><em></em></div>
        <div class="srow"><span>facile</span><em></em><i></i><em></em></div>
        <div class="srow srow--cat"><span>Quia nec honesto</span><em></em><em></em><em></em></div>
        <div class="srow"><span>Videamus</span><i></i><i></i><i></i></div>
        <div class="srow"><span>honesto</span><i></i><i></i><em></em></div>
        <div class="srow"><span>compellans</span><i></i><em></em><em></em></div>
        <div class="srow"><span>Democriteum puto</span><em></em><i></i><em></em></div>
        <div class="srow"><span>Respondeat</span><i></i><em></em><em></em></div>
        <div class="srow srow--cat"><span>admirabilia dicamus</span><em></em><em></em><em></em></div>
        <div class="srow"><span>verborum</span><i></i><i></i><em></em></div>
        <div class="srow"><span>quaerimus</span><i></i><em></em><i></i></div>
        <div class="srow"><span>adipiscing</span><i></i><i></i><em></em></div>
        <div class="srow"><span>philosophorum</span><em></em><i></i><em></em></div>
        <div class="srow"><span>Stoicorum</span><i></i><em></em><em></em></div>
        <div class="srow srow--cat"><span>Democriteum puto</span><em></em><em></em><em></em></div>
        <div class="srow"><span>quaerimus</span><i></i><i></i><em></em></div>
        <div class="srow"><span>probarem</span><i></i><em></em><em></em></div>
        <div class="srow"><span>desperationem</span><em></em><i></i><em></em></div>
        <div class="srow"><span>plerumque</span><i></i><em></em><em></em></div>
        <div class="srow"><span>cognitione</span><em></em><i></i><em></em></div>
        <div class="srow"><span>Epicurum</span><i></i><em></em><em></em></div>
        <div class="srow srow--cat"><span>genuit hominem</span><em></em><em></em><em></em></div>
        <div class="srow"><span>Summum</span><i></i><i></i><em></em></div>
        <div class="srow"><span>verborum</span><i></i><em></em><em></em></div>
        <div class="srow"><span>magnificentia</span><em></em><i></i><em></em></div>
        <div class="srow"><span>delectatus</span><i></i><em></em><em></em></div>
      </div>
    </div>
    <p class="services__note">maintenance three plans gold, silver, and bronze, servicing and troubleshooting, &amp;installation.</p>
  </div>

  <div class="panel panel--blue">
    <div class="feature-photo photo photo--warm" style="top:16px;height:110px" role="img" aria-label="Technician in hard hat and high-visibility jacket inspecting a rooftop AC unit"></div>
    <div class="banner" style="top:128px">LOREM IPSUM DOLOR SIT AMET</div>
    <p class="body-copy" style="top:157px">Duo Reges: constructio interrete. Quia nec honesto quic quam honestius nec turpi turpius. Tria genera bonorum; Quid iudicant sensus? Quae qui non vident, nihil umquam magnum ac cognitione dignum amaverunt. Dicet pro me ipsa virtus. Nihil ad rem!</p>
    <div class="feature-photo photo photo--steel" style="top:236px;height:100px" role="img" aria-label="Stainless steel commercial kitchen refrigeration units"></div>
    <div class="banner" style="top:338px">LOREM IPSUM DOLOR SIT AMET</div>
    <p class="body-copy" style="top:367px">constructio interrete. Quia nec honesto quic quam honestius nec turpi turpius. Tria genera bonorum; Quid iudicant sensus? Quae qui non vident, nihil umquam magnum ac cognitione dignum amaverunt. Dicet pro me ipsa virtus.</p>
    <ul class="points">
      <li>dolor sit amet</li><li>dolor sit amet</li>
      <li>dolor sit amet</li><li>dolor sit amet</li>
      <li>dolor sit amet</li><li>dolor sit amet</li>
    </ul>
  </div>
</section>

</body>
</html>
```